Business Card Design

We recently had a new logo designed by Pixel Harbor. Now we want to create new business cards and letterhead that compliment our new logo.

We are audiologists in private practice specializing in hearing evaluations and fitting hearing aids. We want a clean and professional card.

We need business cards for each audiologist. The names and titles are:
Marlene Voss-Kettering, AuD
Audiologist

Jane Pratt, AuD
Audiologist

Corinna Lundt, AuD
Audiologist

We also need a business card with no provider. Just a generic one.

Finally, we need an appointment card. This is what the front desk uses to give to the patient with their next appointment date and time.

Target Market(s)

Our clients tend to be highly educated. They are older so the cards should be clean and easy to read. No squirrely font please.

Industry/Entity Type

Business

Contact Information for Business Card

27831 Birchmont Dr NE, suite 418
Seattle, WA 98177
206-555-0182

Requirements
Must have
• Clean
Easy to read
Professional
Modern but approachable / warm
Should not have
• Other pictures besides the logo

```html
<!DOCTYPE html>
<html lang="en">
<head>
<meta charset="utf-8">
<title>Alderbrook Hearing Services – Business Card</title>
<link rel="stylesheet" href="https://fonts.googleapis.com/css2?family=Open+Sans:ital,wght@0,400;0,600;1,400&display=swap">
<style>
  :root {
    --navy: #1f2d57;
    --slate: #5f6483;
    --teal: #2f9f8a;
    --ink: #141414;
    --card: #ffffff;
    --backdrop-light: #f2f2f2;
    --backdrop-dark: #bdbdbd;
  }
  * { box-sizing: border-box; margin: 0; padding: 0; }
  html, body {
    width: 1200px;
    height: 787px;
    overflow: hidden;
  }
  body {
    background: radial-gradient(ellipse at 50% 35%, var(--backdrop-light) 0%, #dcdcdc 60%, var(--backdrop-dark) 100%);
    font-family: "Open Sans", Verdana, sans-serif;
    position: relative;
  }
  .business-card {
    position: absolute;
    left: 150px;
    top: 136px;
    width: 900px;
    height: 514px;
    background: var(--card);
    box-shadow: 0 10px 30px rgba(0, 0, 0, 0.18);
    padding: 48px 60px 0 88px;
  }
  .business-card__band {
    position: absolute;
    left: 0;
    top: 0;
    bottom: 0;
    width: 26px;
    background: var(--navy);
  }
  .brand {
    display: flex;
    align-items: center;
    gap: 14px;
    height: 84px;
  }
  .brand__dot {
    width: 52px;
    height: 52px;
    border-radius: 50%;
    background: var(--navy);
    flex: none;
  }
  .brand__name {
    font-size: 26px;
    font-weight: 600;
    color: var(--navy);
    line-height: 1.15;
    max-width: 320px;
  }
  .provider {
    margin-top: 40px;
  }
  .provider__name {
    font-size: 58px;
    font-weight: 400;
    color: var(--ink);
    line-height: 1.05;
  }
  .provider__title {
    margin-top: 6px;
    font-size: 25px;
    font-style: italic;
    color: var(--navy);
  }
  .contact {
    list-style: none;
    margin-top: 44px;
  }
  .contact__item {
    display: flex;
    align-items: center;
    gap: 16px;
    font-size: 26px;
    font-style: italic;
    color: var(--ink);
    margin-bottom: 26px;
  }
  .contact__icon {
    width: 26px;
    height: 30px;
    flex: none;
    fill: var(--navy);
  }
</style>
</head>
<body>
  <article class="business-card">
    <div class="business-card__band"></div>

    <header class="brand">
      <span class="brand__dot"></span>
      <span class="brand__name">Alderbrook Hearing Services</span>
    </header>

    <section class="provider">
      <h1 class="provider__name">Jane Pratt, AuD</h1>
      <p class="provider__title">Audiologist</p>
    </section>

    <ul class="contact">
      <li class="contact__item">
        <svg class="contact__icon" viewBox="0 0 24 28" aria-hidden="true">
          <path d="M6 2 L10 2 L11 8 L8 10 C9 14 11 18 14 20 L17 18 L22 21 L21 26 C12 26 3 16 3 6 Z"/>
        </svg>
        <span>98177 206-555-0182</span>
      </li>
      <li class="contact__item">
        <svg class="contact__icon" viewBox="0 0 24 30" aria-hidden="true">
          <path d="M12 1 C6 1 2 5.5 2 11 C2 18 12 29 12 29 C12 29 22 18 22 11 C22 5.5 18 1 12 1 Z M12 15 A4 4 0 1 1 12 7 A4 4 0 1 1 12 15 Z"/>
        </svg>
        <span>27831 Birchmont Dr NE, suite 418 Seattle, WA</span>
      </li>
    </ul>
  </article>
</body>
</html>
```